Next Generation Of Leaders Need Your Touch of Greatness for their Curriculum

Need to have a curriculum book designed for Summit Pathway Mentoring Course. It is for High School & College Students so it needs to be eye-catching and appealing to the eye. There is a total of 10 Lessons (almost like Chapters) that would be done. Probably about 40 pages or so. Have example chapters of what I like attached. Want it clean, clear and sharp.Here is the link to a current chapter. This would be what you would use as the content in your example https://docs.google.com/document/d/1_uWSbTWDI7MmdI47_OXCTTae_Y9M0LMv7d2aG-XO02o/edit?usp=sharingThe logo attached. Also would need access to the file so I can update content down the road.
Updates
Here is the full document that is to be designed.
https://files.quorvendocs.example/doc/3mV8tNq2WzK6rLp4YsD9xFb1HgJ7cEu0/edit?share=open
There is a total of 10 Lessons.
Thank You!
Target Market(s)
Education Teens/ College Students and teachers of them.
Colors
Designer to choose colors to be used in the design.
Requirements
Must have
- A clean feel.
Nice to have
- I have attached some of the ideas I like.
Should not have
- To crowdy. Over designed.

```html
<!DOCTYPE html>
<html lang="en">
<head>
<meta charset="utf-8">
<title>Mission 6 – Your Retirement Dinner</title>
<link rel="stylesheet" href="https://fonts.googleapis.com/css2?family=Montserrat:wght@400;500;600;700;800&display=swap">
<style>
  :root {
    --stage: #75767b;
    --ink: #0f1116;
    --night: #0d1015;
    --gold: #f0b31d;
    --paper: #ffffff;
    --text: #1d1d1f;
    --steel: #2f4b5c;
  }
  * { box-sizing: border-box; margin: 0; padding: 0; }
  html, body { width: 1200px; height: 800px; overflow: hidden; }
  body {
    background: var(--stage);
    font-family: "Montserrat", sans-serif;
    position: relative;
  }
  .page {
    position: absolute;
    top: 102px;
    width: 422px;
    height: 596px;
    overflow: hidden;
  }

  /* Cover */
  .cover { left: 136px; background: var(--night); }
  .cover-band {
    position: absolute; left: 0; top: 65px;
    width: 319px; height: 94px;
    background: var(--gold);
    overflow: hidden;
  }
  .cover-title {
    position: absolute; left: 22px; top: 23px;
    font-size: 45px; font-weight: 800; letter-spacing: 1px;
    color: var(--ink); line-height: 1;
  }
  .cover-number {
    position: absolute; left: 256px; top: -30px;
    font-size: 150px; font-weight: 800; line-height: 1;
    color: var(--ink);
  }
  .cover-subtitle {
    position: absolute; left: 22px; top: 172px;
    font-size: 15px; font-weight: 400; color: #f2f2f2;
  }
  .cover-visual {
    position: absolute; left: 0; top: 250px;
    width: 100%; height: 346px;
    background:
      radial-gradient(ellipse 60% 35% at 50% 30%, rgba(150,190,210,0.45), transparent 70%),
      radial-gradient(ellipse 80% 40% at 50% 55%, rgba(47,75,92,0.55), transparent 75%),
      linear-gradient(180deg, var(--night) 0%, #10202b 45%, #0c141b 100%);
  }
  .cover-brand {
    position: absolute; left: 104px; top: 474px;
    width: 214px;
    font-size: 30px; font-weight: 700; line-height: 1;
    color: var(--gold); text-align: center;
    letter-spacing: 0.5px;
  }

  /* Inner page */
  .inner { left: 642px; background: var(--paper); color: var(--text); }
  .running-head {
    position: absolute; left: 0; top: 60px;
    width: 388px; height: 31px;
    background: var(--gold);
    overflow: hidden;
  }
  .running-head-title {
    position: absolute; left: 21px; top: 11px;
    font-size: 9px; font-weight: 500; letter-spacing: 1.3px;
    color: var(--ink);
  }
  .running-head-number {
    position: absolute; left: 369px; top: -6px;
    font-size: 42px; font-weight: 800; line-height: 1;
    color: var(--paper);
  }
  .section-heading {
    position: absolute; left: 21px; top: 124px;
    font-size: 27px; font-weight: 700; color: var(--ink); line-height: 1;
  }
  .focus-text {
    position: absolute; left: 21px; top: 160px; width: 381px;
    font-size: 10.4px; line-height: 12px; text-align: justify;
  }
  .list-block { position: absolute; left: 21px; width: 390px; }
  .list-block h3 { font-size: 10px; font-weight: 700; margin-bottom: 4px; color: var(--ink); }
  .list-block ul { list-style: none; padding-left: 10px; }
  .list-block li { font-size: 7.4px; line-height: 13.6px; position: relative; padding-left: 6px; }
  .list-block li::before {
    content: ""; position: absolute; left: 0; top: 5.5px;
    width: 3px; height: 3px; border-radius: 50%; background: var(--ink);
  }
  .objectives { top: 321px; }
  .materials { top: 398px; }
  .footer-rule {
    position: absolute; left: 6px; top: 584px;
    width: 339px; height: 1px; background: #444;
  }
  .footer-note {
    position: absolute; left: 8px; top: 578px;
    font-size: 5px; color: #333;
  }
  .page-number {
    position: absolute; left: 345px; top: 554px;
    width: 48px; height: 42px;
    background: var(--gold);
    font-size: 24px; font-weight: 800; color: var(--ink);
    display: flex; align-items: center; justify-content: center;
  }
</style>
</head>
<body>

  <section class="page cover">
    <div class="cover-band">
      <h1 class="cover-title">MISSION</h1>
      <span class="cover-number">6</span>
    </div>
    <p class="cover-subtitle">Your Retirement Dinner</p>
    <div class="cover-visual" role="img" aria-label="Dark illuminated corridor with rows of cool blue lights receding into the distance"></div>
    <p class="cover-brand">SUMMIT PATHWAY</p>
  </section>

  <section class="page inner">
    <header class="running-head">
      <span class="running-head-title">YOUR RETIREMENT DINNER</span>
      <span class="running-head-number">6</span>
    </header>

    <h2 class="section-heading">FOCUS:</h2>
    <p class="focus-text">The focus of this mission is all about have the students get clear about what’s really important to them. When students have an opportunity to discover what’s really important to them, it can be the catalyst for them implementing what they have learned throughout Summit Pathway as well help them to make better choices.</p>

    <div class="list-block objectives">
      <h3>Student Learning Objectives:</h3>
      <ul>
        <li>Recognize what is REALLY important to them.</li>
        <li>Evaluate how the decisions and choices they make can impact what’s important to them.</li>
        <li>Utilize process of elimination skills to make the best choice.</li>
      </ul>
    </div>

    <div class="list-block materials">
      <h3>Materials Needed:</h3>
      <ul>
        <li>Handout (Provided Below)</li>
        <li>Pens/Pencil (optional)</li>
        <li>Watch / Timer</li>
      </ul>
    </div>

    <p class="footer-note">© 2005-2019, Mission - Your Retirement Dinner</p>
    <div class="footer-rule"></div>
    <div class="page-number">01</div>
  </section>

</body>
</html>
```